Copperfield interiors PTY LTD

My business specializes in commercial fitout which builds walls, ceilings, doors, uses also materials aluminium in works. Id like to have a logo designed for my company too.

Industry/Entity Type

Business

```html
<!DOCTYPE html>
<html lang="en">
<head>
<meta charset="utf-8">
<title>Copperfield Interiors PTY LTD – Business Card</title>
<link href="https://fonts.googleapis.com/css2?family=Questrial&display=swap" rel="stylesheet">
<style>
  :root {
    --page-bg: #f4f5f7;
    --card-top: #171a1f;
    --card-bottom: #08090b;
    --brand-text: #cfe5ff;
    --brand-dot: #4f9be8;
    --band-dark: #1d2a8c;
    --band-light: #3d93dc;
    --band-text: #0a0f1a;
    --accent-blue: #3f8fe0;
    --muted: #b3bac3;
    --contact: #f3f5f8;
    --divider: #6d737b;
  }
  * { margin: 0; padding: 0; box-sizing: border-box; }
  html, body { width: 1200px; height: 900px; overflow: hidden; }
  body {
    background: var(--page-bg);
    font-family: "Questrial", "Century Gothic", sans-serif;
    position: relative;
  }
  .card {
    position: absolute;
    top: 295px;
    width: 540px;
    height: 310px;
    border-radius: 22px;
    overflow: hidden;
    background: linear-gradient(170deg, var(--card-top), var(--card-bottom));
    box-shadow: 0 10px 28px rgba(0,0,0,0.18);
  }
  .card-front { left: 45px; }
  .card-back {
    left: 615px;
    background: radial-gradient(ellipse at 62% 50%, #1b1f26 0%, #0d0f13 55%, #060708 100%);
  }

  .brand {
    position: absolute;
    display: flex;
    align-items: center;
    gap: 12px;
    color: var(--brand-text);
  }
  .brand-dot {
    width: 30px; height: 30px;
    border-radius: 50%;
    background: var(--brand-dot);
    flex: none;
  }
  .brand-name { line-height: 1; }
  .brand-word {
    display: block;
    font-size: 40px;
    letter-spacing: 1px;
  }
  .brand-sub {
    display: block;
    font-size: 13px;
    letter-spacing: 3px;
    margin-top: 4px;
  }
  .card-front .brand { left: 72px; top: 62px; }
  .card-back .brand { left: 110px; top: 130px; }

  .tagline-band {
    position: absolute;
    left: 0; top: 150px;
    width: 100%; height: 15px;
    background: linear-gradient(90deg, var(--band-dark), var(--band-light) 70%, var(--band-dark));
    color: var(--band-text);
    font-size: 10px;
    letter-spacing: 21px;
    line-height: 15px;
    text-align: center;
    padding-left: 40px;
  }

  .holder {
    position: absolute;
    right: 322px; top: 196px;
    text-align: right;
  }
  .holder-name { font-size: 17px; color: var(--accent-blue); }
  .holder-role { font-size: 11px; color: var(--muted); margin-top: 4px; }

  .divider {
    position: absolute;
    left: 228px; top: 186px;
    width: 1px; height: 102px;
    background: var(--divider);
  }

  .contact-list {
    position: absolute;
    left: 236px; top: 190px;
    list-style: none;
    color: var(--contact);
    font-size: 14px;
    line-height: 19px;
  }
  .contact-list li { display: flex; align-items: flex-start; gap: 4px; }
  .contact-list svg { width: 14px; height: 14px; margin-top: 2px; flex: none; }
  .contact-list .indent { padding-left: 18px; }
</style>
</head>
<body>

  <section class="card card-front" aria-label="Business card front">
    <div class="brand">
      <span class="brand-dot"></span>
      <span class="brand-name">
        <span class="brand-word">COPPERFIELD</span>
        <span class="brand-sub">INTERIORS PTY LTD</span>
      </span>
    </div>

    <div class="tagline-band">COMMERCIAL FITOUTS</div>

    <div class="holder">
      <p class="holder-name">Dana Whitfield</p>
      <p class="holder-role">Manager</p>
    </div>

    <div class="divider"></div>

    <ul class="contact-list">
      <li>
        <svg viewBox="0 0 16 16" aria-hidden="true"><path fill="#3f8fe0" d="M3.5 1.5l2.3 2.6-1.2 1.8c.8 1.9 2.3 3.4 4.2 4.3l1.8-1.2 2.6 2.3-1.4 2.2C6.8 13.2 2.8 9.2 1.3 4.2z"/></svg>
        555-014-2276
      </li>
      <li>
        <svg viewBox="0 0 16 16" aria-hidden="true"><rect x="1.5" y="3.5" width="13" height="9" rx="1" fill="none" stroke="#3f8fe0" stroke-width="1.6"/><path d="M2 4.5l6 4.5 6-4.5" fill="none" stroke="#3f8fe0" stroke-width="1.6"/></svg>
        info@copperfieldinteriors.com
      </li>
      <li>
        <svg viewBox="0 0 16 16" aria-hidden="true"><circle cx="8" cy="8" r="6.3" fill="none" stroke="#3f8fe0" stroke-width="1.4"/><ellipse cx="8" cy="8" rx="2.8" ry="6.3" fill="none" stroke="#3f8fe0" stroke-width="1.2"/><path d="M1.7 8h12.6M2.8 5h10.4M2.8 11h10.4" stroke="#3f8fe0" stroke-width="1.1"/></svg>
        www.copperfieldinteriors.com
      </li>
      <li>
        <svg viewBox="0 0 16 16" aria-hidden="true"><path fill="#3f8fe0" d="M8 1.5l7 6h-2v7H9.5v-4h-3v4H3v-7H1z"/></svg>
        2740 Linden Avenue,
      </li>
      <li class="indent">Fairview, Texas 75069</li>
    </ul>
  </section>

  <section class="card card-back" aria-label="Business card back">
    <div class="brand">
      <span class="brand-dot"></span>
      <span class="brand-name">
        <span class="brand-word">COPPERFIELD</span>
        <span class="brand-sub">INTERIORS PTY LTD</span>
      </span>
    </div>
  </section>

</body>
</html>
```